Fiscal Sponsorship Program Flyer

We are seeking a designer to create a 1-2 flyer that explains our fiscal sponsorship program. This flyer will be used to recruit new projects that might be interested in utilizing our fiscal sponsorship services. The pertinent information about our program can be found in the attached PDF. For users who cannot access the PDF, please try this link: https://files.plovarimedia.net/deck/7QtR2wzoLkVa9pXcJ4nEuYhsT3bGdMf8eKqW5rZxN1yo/view?mode=public

Target Market(s)

New charitable projects that do not yet have their own 501(c)(3) status, and are seeking a fiscal sponsor.

Industry/Entity Type

Nonprofit/Charity

Requirements
Must have
• The flyer must include the language and detail included on the attached PDF. The desire is to reformat this to be more appealing and easy to read.

```html
<!DOCTYPE html>
<html lang="en">
<head>
<meta charset="utf-8">
<title>Harborline Foundation – Fiscal Sponsorship Program Flyer</title>
<link rel="stylesheet" href="https://fonts.googleapis.com/css2?family=Oswald:wght@400;500;600&family=Open+Sans:wght@400;600;700&display=swap">
<style>
:root{
  --navy:#262c3a;
  --navy-deep:#1f2431;
  --red:#c7202a;
  --red-dark:#a8161f;
  --white:#ffffff;
  --paper:#f4f4f5;
  --ink:#3a3f4b;
  --muted:#c9ccd3;
  --bg:#e6e7ea;
}
*{box-sizing:border-box;margin:0;padding:0}
html,body{width:1200px;height:900px;overflow:hidden;background:var(--bg)}
body{font-family:"Open Sans",Arial,sans-serif;color:var(--ink);position:relative}
.page{position:absolute;top:81px;width:570px;height:738px;background:var(--white);overflow:hidden;box-shadow:0 4px 18px rgba(0,0,0,.12)}
.page--front{left:20px}
.page--back{left:610px}
.abs{position:absolute}
.heading{font-family:"Oswald",Arial,sans-serif;text-transform:uppercase;letter-spacing:.3px}

/* Front page */
.program-tag{right:24px;top:12px;font-size:14px;color:var(--red);font-weight:600;border-bottom:1px solid var(--red);padding:0 0 3px 60px;line-height:1.3}
.brand-title{left:24px;top:42px;font-size:34px;font-weight:600;color:var(--navy-deep);line-height:1}
.photo{background:linear-gradient(135deg,#c9b9a6,#8c7a6a 45%,#d9d4cf 80%,#a9a29a)}
.photo--team{left:180px;top:92px;width:390px;height:263px}
.mission{left:0;top:138px;width:250px;height:217px;background:var(--navy);border-top-right-radius:40px;padding:30px 22px 0 22px;color:var(--white)}
.mission h2{font-size:15px;font-weight:500;margin-bottom:12px}
.mission p{font-size:9.5px;line-height:1.45;color:#e3e5ea;margin-bottom:9px}
.definition-band{left:0;top:355px;width:570px;height:100px;background:var(--red);color:var(--white);padding:12px 24px}
.definition-band h3{font-size:12px;font-weight:500;margin-bottom:3px}
.definition-band p{font-size:9px;line-height:1.45}
.values{left:0;top:455px;width:258px;height:283px;background:var(--navy);padding:14px 16px;color:var(--white)}
.values h2{font-size:15px;font-weight:500;margin-bottom:8px}
.value{display:flex;gap:10px;margin-bottom:6px;align-items:flex-start}
.value svg{flex:0 0 24px}
.value h4{font-size:8px;font-weight:700;text-transform:uppercase;line-height:1.3}
.value p{font-size:7.6px;line-height:1.3;color:#dfe2e8}
.philosophy{left:282px;top:480px;width:266px}
.philosophy h2{font-size:22px;font-weight:500;color:var(--navy-deep);line-height:1.15}
.rule-red{width:60px;height:3px;background:var(--red);margin:12px 0 14px}
.philosophy p{font-size:10px;line-height:1.55;margin-bottom:10px;color:var(--ink)}
.footer-curve{right:0;bottom:0}
.footer-url{right:26px;bottom:14px;color:var(--white);font-size:13px;letter-spacing:.5px}

/* Back page */
.photo--meeting{left:0;top:0;width:570px;height:228px;background:linear-gradient(120deg,#b8b3ab,#6f6a64 40%,#d6d3cd 70%,#8e8a84)}
.commitments{left:0;top:228px;width:570px;height:245px;background:var(--navy);color:var(--white);padding:24px 28px 0}
.commitments h2{font-size:14px;font-weight:500;text-align:center;margin-bottom:14px}
.commit-grid{display:grid;grid-template-columns:1fr 1fr;column-gap:26px;row-gap:10px}
.commit{display:flex;gap:10px;align-items:center;font-size:8.5px;line-height:1.4;color:#e6e8ed}
.commit svg{flex:0 0 30px}
.commit-rule{position:absolute;left:28px;right:28px;bottom:12px;height:1px;background:#4a5163}
.fee-area{left:0;top:473px;width:570px;height:265px;background:var(--paper)}
.fee-tab{left:190px;top:458px;width:190px;height:28px;background:var(--navy-deep);color:var(--white);font-size:13px;text-align:center;line-height:28px}
.fee-cards{left:22px;top:502px;width:526px;display:flex;gap:8px}
.fee-card{flex:1;background:var(--white);border:1px solid #dcdde0;height:162px}
.fee-card h3{background:var(--red);color:var(--white);font-size:10px;font-weight:500;text-align:center;padding:5px 0}
.fee-card .tier{color:var(--red);font-weight:700;font-size:10px;padding:8px 10px 3px}
.fee-card ul{list-style:none;padding:0 10px}
.fee-card li{font-size:7.8px;line-height:1.45;padding-left:11px;position:relative;color:var(--ink)}
.fee-card li::before{content:"";position:absolute;left:1px;top:3px;width:5px;height:3px;border-left:1.5px solid var(--red);border-bottom:1.5px solid var(--red);transform:rotate(-45deg)}
.fee-card li.note{padding-left:0}
.fee-card li.note::before{display:none}
</style>
</head>
<body>

<section class="page page--front">
  <div class="abs program-tag">Fiscal Sponsorship Program</div>
  <h1 class="abs heading brand-title">Harborline Foundation</h1>
  <div class="abs photo photo--team" role="img" aria-label="Photo of a smiling team gathered around a table reviewing documents"></div>

  <div class="abs mission">
    <h2 class="heading">Mission &amp; Vision</h2>
    <p>The Harborline Foundation, founded in 2010, exists to support social impact campaigns and organizations through educational, public engagement, and awareness efforts.</p>
    <p>Its vision is to strengthen the capacity of the social impact sector and its leaders by providing top-tier fiscal sponsorship services.</p>
  </div>

  <div class="abs definition-band">
    <h3 class="heading">What is fiscal sponsorship?</h3>
    <p>Fiscal sponsorship refers to the practice of non-profit organizations offering their legal and tax-exempt status to charitable projects or groups engaged in activities related to the sponsoring organization's mission. Fiscal sponsors provide oversight, financial management, and other administrative services to build the capacity of charitable projects.</p>
  </div>

  <div class="abs values">
    <h2 class="heading">Organizational Values</h2>
    <div class="value">
      <svg width="24" height="24" viewBox="0 0 28 28"><circle cx="14" cy="14" r="13" fill="none" stroke="#fff" stroke-width="1.2"/><path d="M14 7l6 2v5c0 4-3 6-6 7-3-1-6-3-6-7V9z" fill="none" stroke="#c7202a" stroke-width="1.5"/></svg>
      <div><h4>Trust:</h4><p>We believe that all successful partnerships begin with a foundation of trust.</p></div>
    </div>
    <div class="value">
      <svg width="24" height="24" viewBox="0 0 28 28"><circle cx="14" cy="14" r="13" fill="none" stroke="#fff" stroke-width="1.2"/><path d="M7 15l4-4 3 2 3-2 4 4-5 4z" fill="none" stroke="#c7202a" stroke-width="1.5"/></svg>
      <div><h4>Relationships:</h4><p>Our partners are central to our work. We honor our relationships through respect, communication and transparency.</p></div>
    </div>
    <div class="value">
      <svg width="24" height="24" viewBox="0 0 28 28"><circle cx="14" cy="14" r="13" fill="none" stroke="#fff" stroke-width="1.2"/><path d="M14 7v14M8 10h12M8 10l-2 5h4zM20 10l-2 5h4z" fill="none" stroke="#c7202a" stroke-width="1.4"/></svg>
      <div><h4>Embrace complexity and risk:</h4><p>We understand that bold solutions to intractable social issues often require both complexity and risk.</p></div>
    </div>
    <div class="value">
      <svg width="24" height="24" viewBox="0 0 28 28"><circle cx="14" cy="14" r="13" fill="none" stroke="#fff" stroke-width="1.2"/><circle cx="14" cy="14" r="5" fill="none" stroke="#c7202a" stroke-width="1.5"/><path d="M14 6v3M14 19v3M6 14h3M19 14h3" stroke="#c7202a" stroke-width="1.5"/></svg>
      <div><h4>Innovation:</h4><p>We embrace continuous improvement, bold creativity and change.</p></div>
    </div>
    <div class="value">
      <svg width="24" height="24" viewBox="0 0 28 28"><circle cx="14" cy="14" r="13" fill="none" stroke="#fff" stroke-width="1.2"/><circle cx="14" cy="9" r="2" fill="#c7202a"/><circle cx="9" cy="18" r="2" fill="#c7202a"/><circle cx="19" cy="18" r="2" fill="#c7202a"/><path d="M14 9L9 18h10z" fill="none" stroke="#c7202a" stroke-width="1"/></svg>
      <div><h4>Diversity:</h4><p>We believe that all voices matter and that effective solutions are created when decision-making is inclusive across social, cultural and economic backgrounds.</p></div>
    </div>
  </div>

  <div class="abs philosophy">
    <h2 class="heading">Fiscal Sponsorship Program Philosophy</h2>
    <div class="rule-red"></div>
    <p>We believe we can accelerate the pace and scale of social change by providing strategic back office support to emerging projects, leaders and ideas.</p>
    <p>By providing light touch administrative and capacity building services, our fiscal sponsorship program takes the administrative burden off the shoulders of leaders and their projects to allow them to focus on what they do best - achieving impact and changing the world.</p>
  </div>

  <svg class="abs footer-curve" width="300" height="52" viewBox="0 0 300 52"><path d="M0 52C10 20 30 4 70 4H300V52Z" fill="var(--red)"/></svg>
  <div class="abs footer-url">www.harborlinefoundation.org</div>
</section>

<section class="page page--back">
  <div class="abs photo--meeting" role="img" aria-label="Photo of colleagues in a meeting around a table with laptops"></div>

  <div class="abs commitments">
    <h2 class="heading">Harborline Foundation - Program Commitments</h2>
    <div class="commit-grid">
      <div class="commit"><svg width="30" height="30" viewBox="0 0 30 30"><circle cx="15" cy="15" r="14" fill="var(--red)"/><circle cx="15" cy="15" r="6" fill="none" stroke="#fff" stroke-width="1.5"/><path d="M15 15l3-3" stroke="#fff" stroke-width="1.5"/></svg><span>Fast, simple and efficient fiscal sponsorship program</span></div>
      <div class="commit"><svg width="30" height="30" viewBox="0 0 30 30"><circle cx="15" cy="15" r="14" fill="var(--red)"/><rect x="9" y="8" width="12" height="14" fill="none" stroke="#fff" stroke-width="1.5"/><path d="M11 12h8M11 15h8M11 18h5" stroke="#fff" stroke-width="1.2"/></svg><span>Easy onboarding process</span></div>
      <div class="commit"><svg width="30" height="30" viewBox="0 0 30 30"><circle cx="15" cy="15" r="14" fill="var(--red)"/><path d="M10 15l4 4 7-8" fill="none" stroke="#fff" stroke-width="2"/></svg><span>Free and fast approval process - our application can be completed in 30 minutes or less. There is no fee to apply, and most projects can expect to receive a response on their application within 2 weeks</span></div>
      <div class="commit"><svg width="30" height="30" viewBox="0 0 30 30"><circle cx="15" cy="15" r="14" fill="var(--red)"/><circle cx="15" cy="12" r="3.5" fill="none" stroke="#fff" stroke-width="1.5"/><path d="M9 22c1-4 11-4 12 0" fill="none" stroke="#fff" stroke-width="1.5"/></svg><span>Dedicated customer service and customization of services, tailored to the individual sponsored project's needs</span></div>
      <div class="commit"><svg width="30" height="30" viewBox="0 0 30 30"><circle cx="15" cy="15" r="14" fill="var(--red)"/><rect x="9" y="10" width="12" height="10" fill="none" stroke="#fff" stroke-width="1.5"/><path d="M12 15h6" stroke="#fff" stroke-width="1.5"/></svg><span>No fees and no minimums; projects of any size are welcome to apply</span></div>
      <div class="commit"><svg width="30" height="30" viewBox="0 0 30 30"><circle cx="15" cy="15" r="14" fill="var(--red)"/><circle cx="11" cy="15" r="3" fill="none" stroke="#fff" stroke-width="1.5"/><circle cx="19" cy="15" r="3" fill="none" stroke="#fff" stroke-width="1.5"/></svg><span>Complex, hybrid structures, partnerships and coalitions are strongly encouraged to apply</span></div>
    </div>
    <div class="commit-rule"></div>
  </div>

  <div class="abs fee-area"></div>
  <div class="abs heading fee-tab">Fee Structure</div>

  <div class="abs fee-cards">
    <article class="fee-card">
      <h3 class="heading">Basic | Fee - 4%</h3>
      <div class="tier">Limited</div>
      <ul>
        <li>Project Fund Set-Up</li>
        <li>Administration and Management</li>
        <li>Financial Management</li>
        <li>Grant Proposal Review</li>
        <li>Grant Contract Review</li>
        <li>Project Reporting</li>
        <li>Insurance</li>
        <li>Annual Audit and Form 990</li>
      </ul>
    </article>
    <article class="fee-card">
      <h3 class="heading">Standard | Fee - 6%</h3>
      <div class="tier">Comprehensive</div>
      <ul>
        <li class="note">Basic Services +</li>
        <li>Customized Financial Reporting</li>
        <li>Monthly Financial Statements</li>
        <li>Subgranting/regranting to U.S. based organizations</li>
        <li>Management of Vendor and Independent Contractors (1099s)</li>
      </ul>
    </article>
    <article class="fee-card">
      <h3 class="heading">Premium | Fee - 10% +</h3>
      <div class="tier">Custom</div>
      <ul>
        <li>Standard Services + custom services tailored to individual project needs</li>
        <li class="note">Customization Options:</li>
        <li>Subgranting/regranting to international organizations</li>
        <li>Lobbying Filings</li>
        <li>Project Audit</li>
        <li>Grant Writing Assistance</li>
        <li>One-on-One Coaching</li>
      </ul>
    </article>
  </div>

  <svg class="abs footer-curve" width="300" height="52" viewBox="0 0 300 52"><path d="M0 52C10 20 30 4 70 4H300V52Z" fill="var(--red)"/></svg>
  <div class="abs footer-url">www.harborlinefoundation.org</div>
</section>

</body>
</html>
```